BLQ Business Card

We need a business card that reflect our business, we have put anther business card as an example of what we like but please feel free to do your own thing.

Here are the items to be placed on card

Wade Pelham
Amber Harbor Supply
Mobile: 917-555-4820
Office: 516-555-7164
Fax: 866-555-3291
Email: info@amberharborsupply-example.com
Website: amberharborsupply-example.com

I have added raw files to upload

Wade Pelham
Amber Harbor Supply
Mobile: 917-555-4820
Office: 516-555-7164
Fax: 866-555-3291 

Target Market(s)

Natural product manufactures, and retailers and distributors

Industry/Entity Type

Business

Requirements
Must have
• 1. Logo
2. The colors of the company

```html
<!DOCTYPE html>
<html lang="en">
<head>
<meta charset="utf-8">
<title>Amber Harbor Supply – Business Card</title>
<link rel="stylesheet" href="https://fonts.googleapis.com/css2?family=Open+Sans:wght@400;600;700;800&display=swap">
<style>
  :root {
    --bg: #e4e4e4;
    --card-black: #0b0b0b;
    --card-white: #ffffff;
    --brand-green: #6cb33f;
    --ink: #111111;
    --paper-shadow: rgba(0,0,0,0.22);
  }
  * { box-sizing: border-box; margin: 0; padding: 0; }
  html, body {
    width: 1200px; height: 1012px; overflow: hidden;
    background: var(--bg);
    font-family: "Open Sans", Verdana, sans-serif;
  }
  .stage {
    position: relative; width: 1200px; height: 1012px;
    display: flex; flex-direction: column; align-items: center; justify-content: center; gap: 52px;
  }
  .card {
    position: relative; width: 700px; height: 400px; overflow: hidden;
    box-shadow: 0 6px 18px var(--paper-shadow);
  }

  /* Back side */
  .card-back { background: var(--card-black); color: var(--card-white); }
  .brand-panel {
    position: absolute; left: 70px; top: 26px; width: 560px; height: 126px;
    background: var(--card-white); border-radius: 26px;
    display: flex; align-items: center; justify-content: center; gap: 16px;
  }
  .brand-square { width: 30px; height: 30px; background: var(--brand-green); }
  .brand-name {
    font-weight: 800; font-size: 38px; color: var(--brand-green); letter-spacing: 0.5px;
  }
  .services {
    position: absolute; left: 0; right: 0; top: 176px;
    text-align: center; font-size: 21px; line-height: 29px; font-weight: 400;
  }
  .services .sep { color: var(--brand-green); padding: 0 6px; }
  .back-url {
    position: absolute; left: 0; right: 0; bottom: 30px; text-align: center;
    font-weight: 800; font-size: 25px; color: var(--brand-green);
  }

  /* Front side */
  .card-front { background: var(--card-white); }
  .top-rule { position: absolute; left: 0; top: 0; width: 100%; height: 16px; background: var(--card-black); }
  .name-band {
    position: absolute; left: 0; top: 16px; width: 100%; height: 106px;
    background: var(--brand-green);
    display: flex; align-items: center; justify-content: space-between; padding: 0 40px 0 96px;
  }
  .holder-name {
    color: var(--card-white); font-weight: 700; font-size: 34px; line-height: 36px;
  }
  .band-brand {
    display: flex; align-items: center; gap: 10px;
    color: var(--card-white); font-weight: 800; font-size: 24px;
  }
  .band-brand .brand-square { width: 20px; height: 20px; background: var(--card-white); }
  .contact {
    position: absolute; left: 40px; top: 150px; display: flex;
  }
  .contact-keys {
    display: flex; flex-direction: column; width: 30px; padding-top: 2px;
    color: var(--brand-green); font-size: 20px; line-height: 31px; text-align: center;
  }
  .contact-rule { width: 2px; height: 156px; background: var(--brand-green); margin: 4px 14px 0 2px; }
  .contact-lines {
    list-style: none; color: var(--ink); font-size: 23px; line-height: 31px;
  }
</style>
</head>
<body>
<main class="stage">
  <section class="card card-back" aria-label="Card back">
    <div class="brand-panel">
      <span class="brand-square"></span>
      <span class="brand-name">Amber Harbor Supply</span>
    </div>
    <p class="services">
      Apparel &amp; Accessories<span class="sep">|</span>Bath &amp; Body<br>
      Beverages<span class="sep">|</span>Books<span class="sep">|</span>Bulk<span class="sep">|</span>Food Service<br>
      Fresh Food<span class="sep">|</span>Frozen<span class="sep">|</span>Grocery<br>
      Herbs &amp; Supplements<span class="sep">|</span>Household<span class="sep">|</span>Snacks
    </p>
    <p class="back-url">amberharborsupply-example.com</p>
  </section>

  <section class="card card-front" aria-label="Card front">
    <div class="top-rule"></div>
    <header class="name-band">
      <h1 class="holder-name">Wade<br>Pelham</h1>
      <div class="band-brand"><span class="brand-square"></span>Amber Harbor Supply</div>
    </header>
    <div class="contact">
      <div class="contact-keys"><span>M</span><span>T</span><span>F</span><span>E</span><span>W</span></div>
      <div class="contact-rule"></div>
      <ul class="contact-lines">
        <li>917-555-4820</li>
        <li>516-555-7164</li>
        <li>866-555-3291</li>
        <li>info@amberharborsupply-example.com</li>
        <li>amberharborsupply-example.com</li>
      </ul>
    </div>
  </section>
</main>
</body>
</html>
```